Email Signature

We need a generic email signature designed for our buiding company called 'Birchfield Dwellings'.
We need the following included:
- Name
- Job title (Sales Consultant)
- Phone number
- Mobile number
- Email address
- Physical address
- Web addresss
Please look at the files I have uploaded as these will give you a good idea on our current branding. Our current email signature works well but just needs refreshing! I've also uploaded some images which can be used if needed.
Industry/Entity Type
It Company
Requirements
Nice to have
- If you could incorporate the colours used on the brochure example (contents list) and and arrows on the bottom of the letterhead... just a thought!

```html
<!DOCTYPE html>
<html lang="en">
<head>
<meta charset="utf-8">
<title>Birchfield Dwellings – Email Signature</title>
<link rel="stylesheet" href="https://fonts.googleapis.com/css2?family=Montserrat:wght@700&family=Questrial&display=swap">
<style>
  :root {
    --brand-red: #a01200;
    --ink: #1a1a1a;
    --paper: #ffffff;
    --edge: #d6d6d6;
  }
  html, body {
    margin: 0;
    padding: 0;
    overflow: hidden;
    background: var(--paper);
  }
  .signature {
    position: relative;
    width: 1200px;
    height: 801px;
    box-sizing: border-box;
    border: 2px solid var(--edge);
    background: var(--paper);
    overflow: hidden;
    font-family: "Questrial", sans-serif;
    color: var(--ink);
  }
  .brand {
    position: absolute;
    top: 100px;
    right: 90px;
    display: flex;
    align-items: center;
    gap: 22px;
  }
  .brand-mark {
    width: 70px;
    height: 70px;
    background: var(--brand-red);
  }
  .brand-name {
    font-family: "Questrial", sans-serif;
    font-size: 60px;
    line-height: 1;
    color: var(--brand-red);
    letter-spacing: -0.5px;
  }
  .person {
    position: absolute;
    right: 90px;
    top: 308px;
    text-align: right;
  }
  .person-name {
    margin: 0;
    font-family: "Montserrat", sans-serif;
    font-weight: 700;
    font-size: 36px;
    line-height: 46px;
    color: var(--brand-red);
  }
  .person-role {
    margin: 0;
    font-size: 35px;
    line-height: 46px;
    color: var(--ink);
  }
  .contact {
    position: absolute;
    right: 90px;
    top: 446px;
    margin: 0;
    text-align: right;
    font-style: normal;
    font-size: 33px;
    line-height: 40.5px;
    white-space: nowrap;
  }
  .contact-row { margin: 0; }
  .contact-label { color: var(--brand-red); }
  .contact-value { color: var(--ink); }
  .footer-band {
    position: absolute;
    left: 0;
    bottom: 0;
    width: 100%;
    height: 104px;
    background: var(--brand-red);
  }
</style>
</head>
<body>
  <main class="signature">
    <header class="brand">
      <span class="brand-mark" aria-hidden="true"></span>
      <span class="brand-name">birchfield dwellings</span>
    </header>

    <section class="person">
      <p class="person-name">Name and Lastname</p>
      <p class="person-role">Sales Consultant</p>
    </section>

    <address class="contact">
      <p class="contact-row"><span class="contact-label">Phone</span> <span class="contact-value">03 5198 4420</span></p>
      <p class="contact-row"><span class="contact-label">Mobile</span> <span class="contact-value">0412 738 265</span></p>
      <p class="contact-row"><span class="contact-label">Email</span> <span class="contact-value">yourname@birchfielddwellings.com</span></p>
      <p class="contact-row"><span class="contact-label">Adress</span> <span class="contact-value">18 Foundry Lane, Kelmore Victoria 3871</span></p>
      <p class="contact-row"><span class="contact-label">Web</span> <span class="contact-value">www.birchfielddwellings.com</span></p>
    </address>

    <div class="footer-band" aria-hidden="true"></div>
  </main>
</body>
</html>
```